I want all of this information on my business card.

Derek M. Holloway
President &; CEO

P.O. Box 587302
Auburn Hills, MI 48390

Website: www.GSTbrightsign.com
Email: info@gstbrightsign.com
Cell number: 248-555-0173
Videophone: 313-555-0148

"Your Online ASL Video Textbook"

Please include Logo that is attached.

Target Market(s)

I have an American Sign Language website that attracts, teachers, students learning ASL, parents of deaf children..etc.

Industry/Entity Type

Business

Contact Information for Business Card

Derek M. Holloway
President &; CEO

P.O. Box 587302
Auburn Hills, MI 48390

Cell number: 248-555-0173
Videophone: 313-555-0148

Colors

Designer to choose colors to be used in the design.

Requirements
Must have
• It MUST look professional and adult like. Check out my website to match it a little bit? Look at www.GSTbrightsign.com
Nice to have
• A cool looking business card. :)
Should not have
• It should not look like a kid's design.

```html
<!DOCTYPE html>
<html lang="en">
<head>
<meta charset="utf-8">
<title>GST brightsign business card</title>
<link href="https://fonts.googleapis.com/css2?family=Questrial&family=Lato:wght@400;700&family=Arimo:wght@700&display=swap" rel="stylesheet">
<style>
  :root {
    --green: #45b649;
    --black: #0b0b0b;
    --white: #ffffff;
    --ink: #111111;
    --stage: #2b2b2b;
  }
  * { margin: 0; padding: 0; box-sizing: border-box; }
  html, body { width: 1200px; height: 880px; overflow: hidden; }
  body { background: var(--stage); position: relative; font-family: "Lato", sans-serif; }

  .card {
    position: absolute;
    width: 620px; height: 354px;
    overflow: hidden;
    box-shadow: 0 10px 30px rgba(0,0,0,.45);
  }
  .card--front { left: 80px; top: 50px; background: var(--green); }
  .card--back { left: 500px; top: 476px; background: var(--white); }

  /* brand block */
  .brand { position: absolute; display: flex; align-items: center; gap: 14px; white-space: nowrap; }
  .brand__mark { width: 46px; height: 46px; border-radius: 50%; background: var(--ink); flex: none; }
  .brand__text { display: flex; flex-direction: column; }
  .brand__name { font-family: "Questrial", sans-serif; font-size: 54px; line-height: 1; color: var(--ink); letter-spacing: -1px; }
  .brand__caps { font-family: "Arimo", sans-serif; font-weight: 700; font-size: 14.5px; line-height: 1.2; color: var(--white); letter-spacing: .3px; margin-top: 4px; }
  .brand__tagline { font-family: "Arimo", sans-serif; font-weight: 700; font-size: 13px; line-height: 1.2; color: var(--ink); }
  .card--front .brand { left: 50%; top: 112px; transform: translateX(-50%); }
  .card--back .brand { left: 50%; top: 40px; transform: translateX(-50%); }
  .card--back .brand__caps { color: var(--green); }

  .band { position: absolute; left: 0; right: 0; background: var(--black); color: var(--white); text-align: center; }
  .card--front .band { bottom: 0; height: 52px; line-height: 52px; font-size: 15px; letter-spacing: 1.5px; }
  .band__accent { color: var(--green); }

  .card--back .panel { position: absolute; left: 0; right: 0; top: 168px; bottom: 42px; background: var(--green); }
  .card--back .band { bottom: 0; height: 42px; line-height: 42px; font-size: 16px; letter-spacing: 1.5px; }

  .person { position: absolute; left: 28px; top: 16px; text-align: right; width: 250px; color: var(--ink); }
  .person__name { font-size: 22px; font-weight: 700; color: var(--white); }
  .person__role { font-size: 15px; margin-bottom: 12px; }
  .person__addr { font-size: 15px; line-height: 1.3; }

  .divider { position: absolute; left: 300px; top: 18px; width: 2px; height: 100px; background: var(--white); }

  .contact { position: absolute; left: 322px; top: 14px; list-style: none; color: var(--ink); font-size: 15px; }
  .contact li { display: flex; align-items: center; gap: 9px; height: 25px; }
  .contact svg { width: 18px; height: 18px; flex: none; }
</style>
</head>
<body>

<section class="card card--front" aria-label="Business card front">
  <div class="brand">
    <span class="brand__mark"></span>
    <div class="brand__text">
      <span class="brand__name">GST brightsign</span>
      <span class="brand__caps">AMERICAN SIGN LANGUAGE</span>
      <span class="brand__tagline">Education...One Sign at a Time</span>
    </div>
  </div>
  <div class="band">www.<span class="band__accent">GSTbrightsign</span>.com</div>
</section>

<section class="card card--back" aria-label="Business card back">
  <div class="brand">
    <span class="brand__mark"></span>
    <div class="brand__text">
      <span class="brand__name">GST brightsign</span>
      <span class="brand__caps">AMERICAN SIGN LANGUAGE</span>
      <span class="brand__tagline">Education...One Sign at a Time</span>
    </div>
  </div>

  <div class="panel">
    <div class="person">
      <p class="person__name">Derek M. Holloway</p>
      <p class="person__role">President &amp; CEO</p>
      <p class="person__addr">P.O. Box 587302<br>Auburn Hills, MI 48390</p>
    </div>
    <div class="divider"></div>
    <ul class="contact">
      <li>
        <svg viewBox="0 0 18 18"><circle cx="9" cy="9" r="8" fill="none" stroke="#fff" stroke-width="1.4"/><rect x="6.3" y="4.5" width="5.4" height="9" rx="1" fill="#fff"/></svg>
        248-555-0173
      </li>
      <li>
        <svg viewBox="0 0 18 18"><circle cx="9" cy="9" r="8" fill="none" stroke="#fff" stroke-width="1.4"/><rect x="4.5" y="5.5" width="9" height="6" rx="1" fill="#fff"/><rect x="7.5" y="11.5" width="3" height="1.5" fill="#fff"/></svg>
        313-555-0148
      </li>
      <li>
        <svg viewBox="0 0 18 18"><circle cx="9" cy="9" r="8" fill="none" stroke="#fff" stroke-width="1.4"/><rect x="4.5" y="6" width="9" height="6" fill="#fff"/><path d="M4.5 6 L9 9.5 L13.5 6" fill="none" stroke="#45b649" stroke-width="1"/></svg>
        info@gstbrightsign.com
      </li>
      <li>
        <svg viewBox="0 0 18 18"><circle cx="9" cy="9" r="8" fill="none" stroke="#fff" stroke-width="1.4"/><circle cx="9" cy="9" r="4.5" fill="none" stroke="#fff" stroke-width="1.2"/><path d="M4.5 9 H13.5 M9 4.5 V13.5" stroke="#fff" stroke-width="1"/></svg>
        www.GSTbrightsign.com
      </li>
    </ul>
  </div>
  <div class="band">Your Online ASL Video Textbook</div>
</section>

</body>
</html>
```